Cedar Hall letterhead

We changed our name and logo now need letterhead.
3-4/72 Harlow Street Elmvale 2190
www.cedarhall.org.au
info@cedarhall.org.au
ph: 02 97584120

At this stage, we are preferencing Design #: 5398880 and Design #5401338

```html
<!DOCTYPE html>
<html lang="en">
<head>
<meta charset="utf-8">
<title>Cedar Hall Letterhead</title>
<link rel="stylesheet" href="https://fonts.googleapis.com/css2?family=Montserrat:wght@300;500&family=Open+Sans:wght@400;600&display=swap">
<style>
  :root {
    --backdrop: #ececec;
    --paper: #ffffff;
    --slate: #5d7b8d;
    --slate-dark: #3e5666;
    --slate-line: #6f8c9d;
    --mark-fill: #dde3e8;
    --mark-ring: #8ea3b0;
    --mark-text: #f7f9fa;
    --ink: #2f3a42;
  }
  * { box-sizing: border-box; margin: 0; padding: 0; }
  html, body {
    width: 1200px;
    height: 900px;
    overflow: hidden;
    background: var(--backdrop);
  }
  .stage {
    width: 1200px;
    height: 900px;
    display: flex;
    align-items: center;
    justify-content: center;
  }
  .letterhead {
    position: relative;
    width: 600px;
    height: 848px;
    background: var(--paper);
    box-shadow: 0 2px 10px rgba(0,0,0,0.12);
    overflow: hidden;
  }
  .header-band {
    position: absolute;
    top: 34px;
    left: 22px;
    right: 22px;
    height: 44px;
    background: var(--slate);
    display: flex;
    align-items: center;
    justify-content: flex-end;
    padding-right: 44px;
  }
  .header-rule {
    position: absolute;
    top: 82px;
    left: 22px;
    right: 22px;
    height: 3px;
    background: var(--slate-line);
  }
  .header-name {
    font-family: "Montserrat", sans-serif;
    font-weight: 500;
    font-size: 30px;
    letter-spacing: 4px;
    color: var(--paper);
    text-transform: uppercase;
    line-height: 1;
  }
  .header-seal {
    position: absolute;
    top: 28px;
    left: 32px;
    width: 60px;
    height: 60px;
    border-radius: 50%;
    background: var(--slate);
    border: 3px solid var(--mark-ring);
  }
  .corner-mark {
    position: absolute;
    right: -44px;
    bottom: 100px;
    width: 270px;
    height: 270px;
    border-radius: 50%;
    background: var(--mark-fill);
  }
  .corner-mark-name {
    position: absolute;
    left: 600px;
    bottom: 150px;
    transform: translateX(-100%);
    padding-right: 10px;
    font-family: "Montserrat", sans-serif;
    font-weight: 300;
    font-size: 46px;
    line-height: 1;
    color: var(--mark-text);
    text-transform: uppercase;
    white-space: nowrap;
  }
  .footer {
    position: absolute;
    left: 40px;
    right: 40px;
    bottom: 48px;
    font-family: "Open Sans", sans-serif;
    font-size: 11px;
    color: var(--ink);
  }
  .footer-details {
    display: flex;
    justify-content: space-between;
    align-items: flex-end;
    margin-bottom: 8px;
  }
  .footer-email { font-weight: 600; }
  .footer-address { font-style: normal; text-align: center; line-height: 1.4; margin-bottom: 6px; }
  .footer-web { align-self: flex-start; margin-bottom: 20px; }
  .footer-rule {
    height: 5px;
    background: linear-gradient(90deg, var(--slate-dark), var(--slate-line));
  }
</style>
</head>
<body>
  <main class="stage">
    <article class="letterhead">
      <header>
        <div class="header-band">
          <h1 class="header-name">Cedar Hall</h1>
        </div>
        <div class="header-rule"></div>
        <div class="header-seal" aria-hidden="true"></div>
      </header>

      <div class="corner-mark" aria-hidden="true"></div>
      <span class="corner-mark-name" aria-hidden="true">Cedar<br>Hall</span>

      <footer class="footer">
        <div class="footer-details">
          <span class="footer-email">info@cedarhall.org.au</span>
          <address class="footer-address">
            3-4/72 Harlow Street Elmvale 2190<br>
            ph: 02 97584120
          </address>
          <span class="footer-web">www.cedarhall.org.au</span>
        </div>
        <div class="footer-rule"></div>
      </footer>
    </article>
  </main>
</body>
</html>
```